Law firm website marketed direct to many individual clients

I need someone to design a very basic website for a law firm that will be very eye catching. It's going to be a single-paged, scrolling website with a small number of folds. I have uploaded a simple word document that outlines the basics of what I thought could be the layout, but I am open to suggestion on font, size, shades of color, organization, etc. etc. Essentially the website just needs to be a very efficient and visually appealing way of conveying some simple messages.

Target Market(s)

High volumes of individuals who have gotten into a car accident and then google on their phones a lawyer to hire to represent them.

Industry/Entity Type

Legal

Number of Pages Required

1 page

Font styles to use
Serif
Sans Serif

Colors
34a7d7
85cae6
0592cd

Requirements
Must have
• Must be bright and grab the users attention with color scheme and layout. The different sections should be done in such a way that they can fit entirely onto one smart phone or tablet screen.
Nice to have
• I'd like to try and see what it looks like if in the middle somewhere there is a fold that says "MEET YOUR ATTORNEYS" and includes individual photos of two attorneys, one on the left side and one on the right. And then a small bio section on them. I don't want the photos to include a square or rectangle background, I want the person in the photo to be superimposed on top of whatever pattern or background you have in the fold.
Should not have
• Do not want too much text. Anything more than 2 sentences in any single place is unacceptable.

```html
<!DOCTYPE html>
<html lang="en">
<head>
<meta charset="utf-8">
<title>Meridian Law Group</title>
<link rel="stylesheet" href="https://fonts.googleapis.com/css2?family=Archivo+Black&family=Fira+Sans:wght@300;400;500&display=swap">
<style>
:root{
  --blue:#0592cd;
  --mid:#34a7d7;
  --light:#85cae6;
  --pale:#e6f3fa;
  --text:#555d63;
  --dark:#2a2f33;
  --white:#ffffff;
}
*{margin:0;padding:0;box-sizing:border-box}
html,body{width:1200px;height:2936px;overflow:hidden;background:var(--white)}
body{position:relative;font-family:"Fira Sans",Arial,sans-serif;color:var(--text)}
.abs{position:absolute}
.display{font-family:"Archivo Black","Arial Black",sans-serif;letter-spacing:1px}

/* hero */
.hero{left:0;top:0;width:1200px;height:752px}
.hero-bg{position:absolute;inset:0}
.brand{left:74px;top:26px;color:var(--white);font-family:"Archivo Black",sans-serif;font-size:30px;line-height:1;letter-spacing:1px;display:flex;align-items:center;gap:12px}
.brand-dot{width:16px;height:16px;border-radius:50%;background:var(--white)}
.top-phone{right:74px;top:40px;color:var(--white);font-weight:500;font-size:28px;display:flex;align-items:center;gap:10px}
.hero-kicker{left:0;width:1200px;top:226px;text-align:center;color:var(--white);font-weight:300;font-size:31px}
.hero-title{left:0;width:1200px;top:322px;text-align:center;color:var(--white);font-size:56px;line-height:62px}
.hero-call{left:0;width:1200px;top:502px;text-align:center;color:var(--white);font-weight:300;font-size:34px}
.learn{left:0;width:1200px;top:686px;text-align:center;color:var(--white);font-size:16px}
.scroll-btn{left:584px;top:728px;width:32px;height:32px}

/* features */
.feature{width:260px;text-align:center}
.feature svg{display:block;margin:0 auto}
.feature h3{font-weight:300;color:var(--mid);font-size:24px;line-height:26px;margin-top:8px}
.feature p{font-size:15px;line-height:22px;margin-top:16px;padding:0 20px}
.call-label{left:0;width:1200px;text-align:center;font-size:24px;font-weight:300}
.call-number{left:0;width:1200px;text-align:center;color:var(--blue);font-size:56px}

/* band */
.band{left:0;top:1336px;width:1200px;height:598px;background:linear-gradient(90deg,#f4f8fb 0%,#e9f1f6 45%,#dfe8ee 60%)}
.band-photo{right:0;top:0;width:676px;height:598px;background:linear-gradient(100deg,#c9d6df 0%,#3a4753 18%,#2b3540 55%,#46525e 100%)}
.band h2{font-weight:300;color:var(--blue);font-size:32px}
.band p{font-size:16px;line-height:24px;color:var(--text)}
.band-call{left:0;top:457px;width:524px;height:141px;background:var(--light);color:var(--white);text-align:center}
.band-call span{display:block}

/* attorneys */
.meet{left:0;width:1200px;top:2022px;text-align:center;font-size:24px;font-weight:300;color:var(--dark)}
.meet-title{left:0;width:1200px;top:2052px;text-align:center;color:var(--blue);font-size:56px}
.portrait{width:262px;height:262px;border-radius:50%;border:8px solid var(--pale);background:radial-gradient(circle at 50% 40%,#c9d3db 0%,#8a96a0 55%,#3b4550 100%)}
.divider{left:599px;top:2168px;width:1px;height:386px;background:#e4e8eb}
.att-name{font-size:23px;font-weight:300;color:var(--blue)}
.att-role{font-size:13px;color:var(--text);margin-top:6px}
.att-years{font-size:13px;color:var(--mid);margin-top:6px}
.att-rule{width:2px;height:70px;background:var(--mid)}
.att-bio{width:220px;font-size:16px;line-height:24px}

/* social + footer */
.social{top:2650px;height:56px;color:var(--white);font-size:18px;font-weight:300;display:flex;align-items:center;justify-content:center;gap:14px}
.social-a{left:0;width:600px;background:var(--mid)}
.social-b{left:600px;width:600px;background:var(--blue)}
.social i{width:20px;height:20px;border-radius:50%;background:var(--white);display:block}
.foot-col{top:2746px;width:250px}
.foot-col h4{font-weight:400;color:var(--mid);font-size:18px;margin-bottom:14px}
.foot-col p{font-size:14px;line-height:23px;color:var(--text)}
.news{left:883px;top:2788px;width:244px;height:44px;border:1px solid #dde3e7;display:flex;align-items:center;justify-content:space-between;padding:0 10px 0 14px;font-size:13px;color:#9aa3a9}
.news b{width:24px;height:24px;border-radius:50%;background:var(--light);display:flex;align-items:center;justify-content:center}
.copy{left:0;width:1200px;top:2902px;text-align:center;font-size:13px}
</style>
</head>
<body>

<header class="abs hero">
  <div class="hero-bg" role="img" aria-label="Office desk with laptop and coffee cup in blue tones" style="background:linear-gradient(180deg,#3a8fc9 0%,#1f7fc0 45%,#0b70b4 100%);clip-path:polygon(0 0,1200px 0,1200px 706px,600px 752px,0 706px)"></div>
  <div class="abs brand"><span class="brand-dot"></span>MERIDIAN LAW GROUP</div>
  <div class="abs top-phone">
    <svg width="24" height="24" viewBox="0 0 24 24" fill="none" stroke="#fff" stroke-width="2"><path d="M5 3h4l2 5-3 2a12 12 0 0 0 6 6l2-3 5 2v4a2 2 0 0 1-2 2A17 17 0 0 1 3 5a2 2 0 0 1 2-2z"/></svg>
    504-555-0142
  </div>
  <div class="abs hero-kicker">Accident? Injured?</div>
  <h1 class="abs hero-title display">YOUR CASE<br>YOUR MONEY</h1>
  <div class="abs hero-call">Call 504-555-0142</div>
  <div class="abs learn">Learn More</div>
  <svg class="abs scroll-btn" viewBox="0 0 32 32"><circle cx="16" cy="16" r="14" fill="#fff" stroke="#34a7d7" stroke-width="2"/><path d="M10 13l6 6 6-6" fill="none" stroke="#34a7d7" stroke-width="2"/></svg>
</header>

<section>
  <div class="abs feature" style="left:64px;top:936px">
    <svg width="260" height="126" viewBox="0 0 260 126"><path d="M10 126 A120 120 0 0 1 250 126" fill="none" stroke="#85cae6" stroke-width="3"/><circle cx="130" cy="52" r="52" fill="#85cae6"/><rect x="108" y="36" width="44" height="32" rx="4" fill="none" stroke="#fff" stroke-width="2.5"/><circle cx="130" cy="52" r="7" fill="none" stroke="#fff" stroke-width="2.5"/></svg>
    <h3>Low Fees</h3>
    <p>We charge less, so you keep more.</p>
  </div>
  <div class="abs feature" style="left:334px;top:854px">
    <svg width="260" height="126" viewBox="0 0 260 126"><path d="M10 126 A120 120 0 0 1 250 126" fill="none" stroke="#85cae6" stroke-width="3"/><circle cx="130" cy="52" r="52" fill="#85cae6"/><rect x="112" y="38" width="36" height="22" rx="2" fill="none" stroke="#fff" stroke-width="2.5"/><path d="M104 66h52" stroke="#fff" stroke-width="2.5"/></svg>
    <h3>Free<br>Consultation</h3>
    <p>It's Always Free To Talk To Us.</p>
  </div>
  <div class="abs feature" style="left:604px;top:854px">
    <svg width="260" height="126" viewBox="0 0 260 126"><path d="M10 126 A120 120 0 0 1 250 126" fill="none" stroke="#85cae6" stroke-width="3"/><circle cx="130" cy="52" r="52" fill="#85cae6"/><path d="M117 36h7l3 8-5 3a18 18 0 0 0 9 9l3-5 8 3v7a3 3 0 0 1-3 3A27 27 0 0 1 114 39a3 3 0 0 1 3-3z" fill="none" stroke="#fff" stroke-width="2.5"/></svg>
    <h3>Get Started Using<br>Only Your Phone</h3>
    <p>No Need To Come To The Office, Sign Up Using Your Phone.</p>
  </div>
  <div class="abs feature" style="left:888px;top:936px">
    <svg width="260" height="126" viewBox="0 0 260 126"><path d="M10 126 A120 120 0 0 1 250 126" fill="none" stroke="#85cae6" stroke-width="3"/><circle cx="130" cy="52" r="52" fill="#85cae6"/><rect x="110" y="42" width="40" height="28" rx="3" fill="none" stroke="#fff" stroke-width="2.5"/><path d="M122 42v-6h16v6M110 54h40" fill="none" stroke="#fff" stroke-width="2.5"/></svg>
    <h3>Speak Directly To<br>A Lawyer</h3>
    <p>No Staff Screening. Talk Right To A Lawyer On Your First Call.</p>
  </div>
  <div class="abs call-label" style="top:1160px">Call</div>
  <div class="abs call-number display" style="top:1186px">504-555-0142</div>
</section>

<section class="abs band">
  <div class="abs band-photo" role="img" aria-label="Attorney in a dark suit with arms crossed"></div>
  <h2 class="abs" style="left:74px;top:76px">No Fee Unless We Win</h2>
  <p class="abs" style="left:74px;top:128px;width:420px">We Don't Get Paid Unless You Get Paid. It's As Simple As That. We Let Our Results Do The Talking For Us.</p>
  <h2 class="abs" style="left:74px;top:230px">Questions About Anything?</h2>
  <p class="abs" style="left:74px;top:284px;width:430px">We're Here To Help. Feel Free To Call Us At 504-555-0142 To Speak To One Of Our Attorneys. With Extensive Experience In Helping Clients Get The Results That They Want, Our Team Is Always Just A Phone Call Away.</p>
  <div class="abs band-call">
    <span style="font-size:24px;font-weight:300;margin-top:18px">Call</span>
    <span class="display" style="font-size:56px;line-height:64px">504-555-0142</span>
  </div>
</section>

<section>
  <div class="abs meet">Meet Your</div>
  <h2 class="abs meet-title display">ATTORNEYS</h2>
  <div class="abs portrait" style="left:155px;top:2169px" role="img" aria-label="Portrait of attorney Harlan Price"></div>
  <div class="abs portrait" style="left:783px;top:2169px" role="img" aria-label="Portrait of attorney Dorian Wells"></div>
  <div class="abs divider"></div>

  <div class="abs" style="left:74px;top:2462px">
    <div class="att-name">Harlan Price</div>
    <div class="att-role">Attorney</div>
    <div class="att-years">14 Years of practice</div>
  </div>
  <div class="abs att-rule" style="left:252px;top:2468px"></div>
  <p class="abs att-bio" style="left:290px;top:2462px">Lorem Ipsum, giving information on its origins, as well as a random Lipsum generator.</p>

  <div class="abs" style="left:703px;top:2462px">
    <div class="att-name">Dorian Wells</div>
    <div class="att-role">Attorney</div>
    <div class="att-years">18 Years of practice</div>
  </div>
  <div class="abs att-rule" style="left:881px;top:2468px"></div>
  <p class="abs att-bio" style="left:918px;top:2462px">Lorem Ipsum, giving information on its origins, as well as a random Lipsum generator.</p>
</section>

<footer>
  <div class="abs social social-a"><i></i>Follow Us On Socialhub</div>
  <div class="abs social social-b"><i></i>Follow Us On Chirpline</div>

  <div class="abs foot-col" style="left:74px">
    <h4>Come and Visit</h4>
    <p>Meridian Law Group<br>100 Harbor Street Suite 4<br>Riverside, La 70000</p>
  </div>
  <div class="abs foot-col" style="left:344px">
    <h4>Get In Touch</h4>
    <p>504-555-0142<br>info@meridianlawgroup.com</p>
  </div>
  <div class="abs foot-col" style="left:613px">
    <h4>Recommended</h4>
    <p>Terms of Use<br>Privacy Policy</p>
  </div>
  <div class="abs foot-col" style="left:883px">
    <h4>Signup Newsletter</h4>
  </div>
  <div class="abs news">Email Address<b><svg width="10" height="10" viewBox="0 0 10 10"><path d="M3 1l4 4-4 4" fill="none" stroke="#fff" stroke-width="2"/></svg></b></div>
  <div class="abs copy">© 2016 Meridian Law Group. All Rights Reserved.</div>
</footer>

</body>
</html>
```